Wine Label Design-Crimson Gully Vineyard

Crimson Gully Vineyard is in the Barossa Valley in South Australia. The Barossa is recognized as Australia's premier wine region, producing Australia's icon wines and some " new takes on traditional".
This family owned and operated vineyard grows some exceptionally high quality fruit. Most of the fruit is sold and used for some of Australia's most iconic wines. Small quantities are retained by the owners for some wines with very limited availability. (Wines were previously sold as Pellow Draycott Vineyards Crimson Gully ( Shiraz, Cabernet etc).

The wines will in the future be labeled simply ‘Crimson Gully Vineyard’. The label will launch this new identity for the single family single vineyard and its high quality wines which are a true expression of the vineyard and derive from the Crimson Gully common to this ancient area (800-2000 million years old).
The label should reflect
• Single vineyard, family owned
• vines in very old rock & soils
• High quality & reliability
• Edgy but true, design based thinking (Please note:blue is generally seen as an unacceptable colour for a wine label?? Don’t ask me why)

The wines will be sold mostly direct in Australia ( ie not through retail stores), with limited export to Asia, Scandinavia and Canada.
There are three quality levels and price points in the portfolio
1. Entry level premium for everyday drinking for discriminating drinkers-approx AUD20
2. Super Premium-approx AUD30
3. Limited Release ultlra premium-AUD75-90?
We envisage three variations on the label but with an obvious & common design element. This design element should be able to be used for corporate identification and promotion
The paper stock will be waterproof and self adhesive. Our preference is for designs that engage the user by appealing to both sight and touch. It is preferred that textures be added eg embossing, high build varnish etc-rather than be a facet of the stock itself.
For information on statutory label requirements refer to www.vintnerregistry-example.com . In brief
o Front label need not show any mandatory information. However we would prefer Variety, Barossa Valley, Year and alcohol to be shown on the front label
o Back label should show all mandatories and allow for a bar code

Project Deadline Extended
Reason: I've had a problem with my wireless broadband account and reception has been intermittent to say the least to the extent that I switched off at the weekend. Just going downtown now for a 'polite discussion' with my service provider.

Project Deadline Extended
Reason: I have receiver insufficient designs of quality which we would consider. Too many designs have a "cut and paste" appearance - too few exhibit an original art/design element which truly identifies the product.

Gals & Guys

most of the designs submitted lack punch and originality and are totally unmemorable.
Please-get on Google or whatever enter "Wine Label Designs" and do some research b4 u waste your time and mine. Formulaic cut and paste will not win the day. That's not to say that cut and paste can't work-but it must have some originality, impact and command attention. Please surprise me.

Following on from a question from a designer about who is our competition and what we are looking for I sent the following 
"I don't think I can add anything new. Read the brief and comments again and research wine labels on the web. In 30 minutes you'll get a good idea of the creative edgy designs in the industry. There are a plethora of collections. Our competition-anyone with a label. In 2010 there were over 2400 "producers" in other words 2400 producers with at least one label. In fact there are over 25000 Australian wines and then the numerous imported wines.

Target Market(s)

$20 people who budget everyday but have graduated from drinking 'entry level' wines. These people will likely fit into Cat. (b) in the $30 wine

$30 (a) will not over-compromise on some everyday discretionary expenditure.(b) might buy for special occasions

$70-$90 Professional/successful people with high disposable/discretionary income not particularly worried about recession. wine geeks.

Industry/Entity Type

Retail

Requirements
Must have
• identifiable element across range of wines

```html
<!DOCTYPE html>
<html lang="en">
<head>
<meta charset="utf-8">
<title>Crimson Gully Vineyard — Cabernet Sauvignon Label Range</title>
<link href="https://fonts.googleapis.com/css2?family=Cinzel:wght@700&family=Crimson+Text:wght@400;700&family=Pinyon+Script&display=swap" rel="stylesheet">
<style>
  :root {
    --page: #ffffff;
    --navy: #0f0a52;
    --gold: #e2b766;
    --gold-soft: #c9a25a;
    --tier-premium: #0b3a9f;
    --tier-super: #067f0a;
    --tier-ultra: #b10b0b;
    --bottle: #1a1414;
    --cap: #b3141a;
  }
  * { box-sizing: border-box; margin: 0; padding: 0; }
  html, body { width: 1200px; height: 900px; overflow: hidden; background: var(--page); }
  .canvas { position: relative; width: 1200px; height: 900px; }

  .label {
    position: absolute;
    width: 391px; height: 346px;
    background: var(--navy);
    border-radius: 24px;
    color: var(--gold);
    font-family: "Crimson Text", serif;
    text-align: center;
  }
  .label--premium { left: 187px; top: 84px; --tier: var(--tier-premium); }
  .label--super   { left: 622px; top: 84px; --tier: var(--tier-super); }
  .label--ultra   { left: 405px; top: 468px; --tier: var(--tier-ultra); }

  .label__frame {
    position: absolute; inset: 10px;
    border: 3px solid var(--gold);
    border-radius: 16px;
  }
  .label__mark {
    position: absolute; left: 0; right: 0; top: 52px;
    display: flex; justify-content: center; align-items: center; gap: 8px;
    font-size: 15px; font-weight: 700; letter-spacing: 0.5px;
  }
  .label__mark-square {
    width: 14px; height: 14px; background: var(--tier);
    border: 2px solid var(--gold);
  }
  .label__rule {
    position: absolute; left: 50%; transform: translateX(-50%);
    height: 1px;
    background: linear-gradient(90deg, transparent, var(--gold) 20%, var(--gold) 80%, transparent);
  }
  .label__rule--top { top: 114px; width: 270px; }
  .label__rule--bottom { top: 162px; width: 240px; }
  .label__name {
    position: absolute; left: 0; right: 0; top: 118px;
    font-family: "Pinyon Script", cursive;
    font-size: 31px; line-height: 40px;
  }
  .label__year {
    position: absolute; left: 0; right: 0; top: 168px;
    font-size: 17px; font-weight: 700; line-height: 20px;
  }
  .label__region {
    position: absolute; left: 0; right: 0; top: 187px;
    font-size: 13px; font-weight: 700; line-height: 16px;
  }
  .label__band {
    position: absolute; left: 13px; right: 13px; top: 218px; height: 56px;
    background: var(--tier);
    border-top: 3px solid var(--gold);
    border-bottom: 3px solid var(--gold);
    padding-top: 5px;
  }
  .label__tier {
    font-family: "Cinzel", serif; font-weight: 700;
    font-size: 19px; letter-spacing: 2.5px; line-height: 22px;
  }
  .label__variety { font-size: 13.5px; line-height: 16px; }
  .label__facts {
    position: absolute; left: 40px; right: 40px; top: 285px;
    display: flex; justify-content: space-between;
    font-size: 12.5px; line-height: 16px;
    padding-bottom: 4px;
    border-bottom: 1px solid var(--gold);
  }
  .label__address {
    position: absolute; left: 0; right: 0; top: 307px;
    font-size: 9.3px; line-height: 12px;
  }

  .bottle { position: absolute; left: 889px; top: 465px; width: 96px; height: 356px; }
  .bottle__label {
    position: absolute; left: 5px; top: 188px;
    width: 391px; height: 346px;
    transform: scale(0.217); transform-origin: 0 0;
    opacity: 0.9;
  }
  .bottle__label .label { left: 0; top: 0; }
</style>
</head>
<body>
<main class="canvas">

  <article class="label label--premium">
    <div class="label__frame"></div>
    <div class="label__mark"><span class="label__mark-square"></span>Crimson Gully</div>
    <div class="label__rule label__rule--top"></div>
    <h2 class="label__name">Crimson Gully Vineyard</h2>
    <div class="label__rule label__rule--bottom"></div>
    <p class="label__year">2006</p>
    <p class="label__region">Barossa Valley - South Australia</p>
    <div class="label__band">
      <p class="label__tier">Premium</p>
      <p class="label__variety">Cabernet Sauvignon</p>
    </div>
    <p class="label__facts"><span>750 mL</span><span>Standard drinks - 8,3</span><span>13,5% ALC/VOL.</span></p>
    <p class="label__address">Crimson Gully Vineyard , Barossa Valley , Mill Lane 14/8, South Australia</p>
  </article>

  <article class="label label--super">
    <div class="label__frame"></div>
    <div class="label__mark"><span class="label__mark-square"></span>Crimson Gully</div>
    <div class="label__rule label__rule--top"></div>
    <h2 class="label__name">Crimson Gully Vineyard</h2>
    <div class="label__rule label__rule--bottom"></div>
    <p class="label__year">2006</p>
    <p class="label__region">Barossa Valley - South Australia</p>
    <div class="label__band">
      <p class="label__tier">Super Premium</p>
      <p class="label__variety">Cabernet Sauvignon</p>
    </div>
    <p class="label__facts"><span>750 mL</span><span>Standard drinks - 8,3</span><span>13,5% ALC/VOL.</span></p>
    <p class="label__address">Crimson Gully Vineyard , Barossa Valley , Mill Lane 14/8, South Australia</p>
  </article>

  <article class="label label--ultra">
    <div class="label__frame"></div>
    <div class="label__mark"><span class="label__mark-square"></span>Crimson Gully</div>
    <div class="label__rule label__rule--top"></div>
    <h2 class="label__name">Crimson Gully Vineyard</h2>
    <div class="label__rule label__rule--bottom"></div>
    <p class="label__year">2006</p>
    <p class="label__region">Barossa Valley - South Australia</p>
    <div class="label__band">
      <p class="label__tier">Ultra Premium</p>
      <p class="label__variety">Cabernet Sauvignon</p>
    </div>
    <p class="label__facts"><span>750 mL</span><span>Standard drinks - 8,3</span><span>13,5% ALC/VOL.</span></p>
    <p class="label__address">Crimson Gully Vineyard , Barossa Valley , Mill Lane 14/8, South Australia</p>
  </article>

  <figure class="bottle" aria-label="Bottle mock-up with the Ultra Premium label">
    <svg width="96" height="356" viewBox="0 0 96 356">
      <path d="M30 40 L66 40 L66 70 C66 92 94 100 94 140 L94 356 L2 356 L2 140 C2 100 30 92 30 70 Z" fill="var(--bottle)"/>
      <rect x="29" y="0" width="38" height="48" rx="2" fill="var(--cap)"/>
      <rect x="41" y="5" width="4" height="38" fill="#e24a4f"/>
      <rect x="32" y="125" width="4" height="220" fill="#ffffff"/>
    </svg>
    <div class="bottle__label">
      <article class="label label--ultra">
        <div class="label__frame"></div>
        <div class="label__mark"><span class="label__mark-square"></span>Crimson Gully</div>
        <div class="label__rule label__rule--top"></div>
        <h2 class="label__name">Crimson Gully Vineyard</h2>
        <div class="label__rule label__rule--bottom"></div>
        <p class="label__year">2006</p>
        <p class="label__region">Barossa Valley - South Australia</p>
        <div class="label__band">
          <p class="label__tier">Ultra Premium</p>
          <p class="label__variety">Cabernet Sauvignon</p>
        </div>
        <p class="label__facts"><span>750 mL</span><span>Standard drinks - 8,3</span><span>13,5% ALC/VOL.</span></p>
        <p class="label__address">Crimson Gully Vineyard , Barossa Valley , Mill Lane 14/8, South Australia</p>
      </article>
    </div>
  </figure>

</main>
</body>
</html>
```